Commercial Cleaning Company Website Design

We are working with Harbor Sweep Team. They are a commercial cleaning company that needs a new website design.

Some sites to use for inspiration:

https://www.plenvask.com
https://glint-panecleaning.com
https://tidyhelpers.net
https://calmnesthouse.com
https://www.thecleaningbureauxyz.com
https://www.dottiebroom.com

Thank you for taking the time to consider designing a website for us. We are web developers based in Stockton and Los Angeles, CA, USA. Most of our projects go through the same process. Understanding this process may help you win a project with us. We custom-code all of our websites in-house. We don’t have any requirements as to what tools you use for your design, but we prefer Figma files. For any design that we label as four-stars, we send it to the client for review. The client picks the final design they want us to use. Once we complete this process, we will continue to show additional clients all the four-star sites and purchase them later. Your designs will have multiple chances to sell. For better chances of success, we ask that you follow these guidelines.

IMAGES:
If you use any images or icons in the design, we ask that you have a link to the asset so we can purchase the image/icon. Most of the designs we submit do not have the customer’s images on them unless they have some great images. Be creative; show us the feeling you are trying to portray with your image choices. Use any royalty-free site you choose. We subscribe to Adobe and mainly use their images, but we can purchase images outside of Adobe.

PLEASE NOTE: we will not submit designs to clients with watermarks on the images.

FONTS:
We ask that you identify the fonts used in the design. This can be done in a message if you want. We typically use Google Fonts and Adobe Fonts.

CONTENT:
We're always open to different content and ideas. We often submit designs with stock images so the client can see our vision. We typically take pictures after the website launch to use their images with our vision. Lorem Ipsum is fine for paragraphs, but we ask that you write the headers in correct English. We want to be able to show the vision and identify the sections of the website.

INSPIRATION:
We typically add a couple of links in the brief of websites we like to help you get started in your design.

REVISIONS:
We do not often ask for revisions of the designs unless we see something in the design that may not appeal to the client. If there are slight changes that we want to make, we do that in the development process.

FEEDBACK:
We rarely give feedback on designs during the design process. We are working on many website projects and do not have the time to provide feedback. We usually respond if your request is well thought out and asks specific questions, but a note asking “feedback, please” usually goes unanswered.

```html
<!DOCTYPE html>
<html lang="en">
<head>
<meta charset="utf-8">
<title>Harbor Sweep Team — Commercial Cleaning</title>
<link href="https://fonts.googleapis.com/css2?family=Inter:ital,wght@0,400;0,500;0,600;0,700;1,500&display=swap" rel="stylesheet">
<style>
:root{
  --blue:#1a4fc4;
  --blue-dark:#143e9c;
  --red:#e5261b;
  --ink:#111827;
  --muted:#6b7280;
  --line:#e3e7ee;
  --soft:#eef3fc;
  --white:#ffffff;
  --stage:#000000;
}
*{margin:0;padding:0;box-sizing:border-box}
html,body{width:1200px;height:1200px;overflow:hidden;background:var(--stage)}
body{font-family:"Inter",sans-serif;color:var(--ink)}
.page{position:absolute;left:495px;top:0;width:1200px;height:6860px;background:var(--white);transform:scale(.1749);transform-origin:0 0;overflow:hidden}
.abs{position:absolute}
.photo{position:absolute}
.label{color:var(--blue);font-size:15px;font-weight:600}
.h2{font-size:42px;font-weight:600;line-height:1.2;color:var(--ink)}
.p{font-size:14px;line-height:1.9;color:var(--muted)}
.btn{display:inline-flex;align-items:center;justify-content:center;background:var(--red);color:#fff;font-size:13px;font-weight:600;height:36px;padding:0 30px}
.center{text-align:center;left:0;right:0}

/* top bar */
.brand{display:flex;align-items:center;gap:10px;font-weight:700;font-size:16px;color:var(--blue);letter-spacing:1px}
.brand .mark{width:16px;height:16px;background:var(--red)}
.info{display:flex;align-items:center;gap:12px;font-size:12px;color:var(--ink)}
.info small{display:block;color:var(--muted);font-size:10px}
.info svg{width:30px;height:30px}
.nav{left:163px;top:100px;width:874px;height:50px;background:var(--blue);display:flex;align-items:center;padding-left:38px;gap:36px;color:#fff;font-size:13px;z-index:3}
.nav .search{margin-left:auto;background:#3a68d6;height:100%;width:130px;display:flex;align-items:center;padding-left:18px;opacity:.95}
.nav .menu{width:50px;height:100%;background:#2f5fd3;display:flex;align-items:center;justify-content:center;margin-left:-36px}

/* hero */
.hero-photo{left:0;top:100px;width:1200px;height:700px;background:linear-gradient(135deg,#d9dde3,#8d949e 60%,#50555d);clip-path:polygon(0 0,100% 0,100% 100%,0 82%)}
.hero-card{left:82px;top:497px;width:507px;height:632px;background:var(--blue);color:#fff;padding:80px 40px 0}
.hero-card h1{font-size:40px;font-weight:600;line-height:1.22;margin:30px 0 16px}
.hero-card p{font-size:15px;line-height:1.75;opacity:.9}
.rate{display:flex;align-items:center;gap:14px;margin-top:60px;font-size:11px}
.avs{display:flex}
.avs span{width:50px;height:50px;border-radius:50%;background:#c9b8a6;border:3px solid var(--blue);margin-right:-12px}
.price{left:632px;top:856px;width:486px;height:273px;border:1px solid var(--line);background:#fff}
.price .head{background:var(--blue);color:#fff;font-size:14px;font-weight:600;height:44px;display:flex;align-items:center;justify-content:center}
.price .cols{display:flex;height:229px}
.price .col{flex:1;text-align:center;padding-top:38px}
.price .col+.col{border-left:1px solid var(--line)}
.price .col h4{font-size:15px;font-weight:600}
.price .tag{display:inline-block;background:var(--red);color:#fff;font-size:24px;font-weight:700;padding:4px 18px;margin:22px 0 18px;border:3px solid #fff;outline:1px solid var(--red)}
.price .col p{font-size:11px;line-height:2;color:var(--muted)}

/* about */
.feat{display:flex;align-items:center;gap:18px;font-size:12px;font-weight:600}
.feat i{width:52px;height:52px;background:var(--soft);display:block}

/* services */
.svc{position:absolute;width:334px;height:415px;border:1px solid var(--line);background:#fff;text-align:center}
.svc .img{height:245px;background:linear-gradient(135deg,#b9c3d0,#6c7a8c)}
.svc h4{font-size:15px;font-weight:600;margin:50px 0 16px}
.svc p{font-size:12px;line-height:1.9;color:var(--muted);padding:0 40px}
.svc.on{background:var(--blue)}.svc.on h4,.svc.on p{color:#fff}
.outline{border:2px solid var(--ink);font-size:12px;font-weight:600;height:36px;width:140px;display:flex;align-items:center;justify-content:center}

/* industries */
.ind{position:absolute;top:3156px;width:194px;height:138px;border:1px solid var(--line);display:flex;flex-direction:column;align-items:center;justify-content:center;gap:14px;font-size:14px;font-weight:500}
.ind i{width:40px;height:40px;border:3px solid var(--red);border-radius:4px;display:block}
.ind.on{background:var(--blue);color:#fff}.ind.on i{border-color:#fff}

/* lists */
.ticks{list-style:none;font-size:12px;color:var(--ink)}
.ticks li{display:flex;align-items:center;gap:14px;height:27px}
.ticks li:before{content:"";width:14px;height:14px;border:2px solid var(--muted);border-radius:50%}

/* plans */
.plan{position:absolute;top:4725px;width:334px;height:440px;background:#fff;border:1px solid var(--line);padding:40px 32px}
.plan .t{display:flex;align-items:center;gap:18px;font-size:15px;font-weight:600}
.plan .t i{width:36px;height:36px;border:3px solid var(--red);display:block}
.plan .amt{font-size:40px;font-weight:600;margin:16px 0 22px}
.plan .amt small{font-size:11px;font-weight:400}
.plan .ticks li{height:30px;font-size:12px}
.plan .btn{width:100%;margin-top:36px}
.plan.on{background:var(--blue);color:#fff;border-color:var(--blue)}
.plan.on .ticks li{color:#fff}.plan.on .t i{border-color:#fff}

/* footer */
.flinks{font-size:12px;line-height:1.9;color:var(--ink)}
.dot{width:22px;height:22px;border-radius:50%;background:var(--blue);display:inline-block;margin-right:4px}
</style>
</head>
<body>
<div class="page">

  <!-- top bar -->
  <div class="abs brand" style="left:82px;top:24px"><span class="mark"></span>HARBOR SWEEP TEAM</div>
  <div class="abs info" style="left:350px;top:20px"><svg viewBox="0 0 24 24" fill="none" stroke="#111" stroke-width="1.4"><rect x="3" y="5" width="18" height="14"/><path d="M3 6l9 7 9-7"/></svg><div><small>Lorem Ipsum Dolor</small>Email To Us</div></div>
  <div class="abs info" style="left:535px;top:20px"><svg viewBox="0 0 24 24" fill="none" stroke="#111" stroke-width="1.4"><circle cx="12" cy="12" r="9"/><path d="M12 7v5l3 2"/></svg><div><small>Sunday To Friday</small>9Am - 08pm</div></div>
  <div class="abs info" style="left:745px;top:20px"><svg viewBox="0 0 24 24" fill="none" stroke="#111" stroke-width="1.4"><path d="M5 4h4l2 5-3 2a11 11 0 0 0 5 5l2-3 5 2v4a2 2 0 0 1-2 2A16 16 0 0 1 3 6a2 2 0 0 1 2-2z"/></svg><div><small>Call Anytime</small>123-456-7890</div></div>
  <div class="abs info" style="left:960px;top:20px"><svg viewBox="0 0 24 24" fill="none" stroke="#111" stroke-width="1.4"><path d="M12 21s-7-7-7-12a7 7 0 0 1 14 0c0 5-7 12-7 12z"/><circle cx="12" cy="9" r="2.5"/></svg><div><small>Lorem Ipsum Dolor</small>United States</div></div>

  <nav class="abs nav"><b>Home ⌄</b><span>About Us</span><span>Services</span><span>Industries Served</span><span>Testimonials</span><span>Contact Us</span><span class="search">⌕ Search...</span><span class="menu">≡</span></nav>

  <!-- hero -->
  <div class="photo hero-photo" role="img" aria-label="Two cleaners vacuuming and wiping desks in a bright open-plan office"></div>
  <div class="abs hero-card">
    <div style="width:22px;height:40px;background:var(--red)"></div>
    <h1>Commercial Cleaning That Elevates Your Workplace</h1>
    <p>Reliable, High-Quality Cleaning Services For Offices, Retail, Medical, Industrial, And More</p>
    <div style="display:flex;align-items:center;gap:12px;margin-top:40px"><span class="btn">Request a Free Quote</span><span style="width:36px;height:36px;border-radius:50%;background:#fff;opacity:.5"></span></div>
    <div class="rate"><div class="avs"><span></span><span></span><span></span></div><div style="margin-left:18px"><span style="color:#f6b800">★★★★★</span> 5.0<br>Rated Best Over 15% Reviews</div></div>
  </div>
  <div class="abs price">
    <div class="head">Special Price This Month</div>
    <div class="cols">
      <div class="col"><h4>Regular Wash</h4><span class="tag">$10.99</span><p>Lorem Ipsum Dolor Sit Amet,<br>Consectetur Adipiscing Elit</p></div>
      <div class="col"><h4>Monthly Wash</h4><span class="tag">$79.99</span><p>Lorem Ipsum Dolor Sit Amet,<br>Consectetur Adipiscing Elit</p></div>
    </div>
  </div>

  <!-- about -->
  <div class="photo" style="left:82px;top:1228px;width:422px;height:629px;background:linear-gradient(160deg,#dfe4ea,#8f98a4 70%,#5d4a3a)" role="img" aria-label="Cleaner washing office windows while a colleague mops the floor"></div>
  <div class="abs" style="left:589px;top:1300px;width:529px">
    <div class="label">About Company</div>
    <div class="h2" style="margin:14px 0 24px">Built On Professionalism &amp; Integrity</div>
    <p class="p" style="font-size:12.5px">Harbor Sweep Team Provides Dependable Commercial Cleaning Throughout California. Our Professionally Trained Staff And Detailed Cleaning Standards Ensure A Consistently Fresh, Healthy, And Productive Workplace.</p>
    <div style="display:grid;grid-template-columns:1fr 1fr;gap:26px 0;margin-top:42px">
      <div class="feat"><i></i>Locally Owned &amp; Operated</div>
      <div class="feat"><i></i>Strict Quality Control</div>
      <div class="feat"><i></i>Background-Checked Professionals</div>
    </div>
    <span class="btn" style="margin-top:44px;padding:0 34px">Learn More</span>
  </div>

  <!-- services -->
  <div class="abs label" style="left:82px;top:1950px">Our Services</div>
  <div class="abs h2" style="left:82px;top:1982px;font-size:38px">Our Commercial Cleaning Services</div>
  <div class="abs outline" style="left:978px;top:1985px">View All</div>
  <div class="svc" style="left:82px;top:2080px"><div class="img" role="img" aria-label="Staff cleaning a busy office"></div><h4>Office Cleaning</h4><p>Lorem Ipsum Dolor Sit Amet, Consectetur Adipiscing Elit, Sed Do Eiusmod Tempor Incididunt Ut</p></div>
  <div class="svc on" style="left:433px;top:2080px"><div class="img" role="img" aria-label="Polished floor in a retail store aisle"></div><h4>Retail Store Cleaning</h4><p>Lorem Ipsum Dolor Sit Amet, Consectetur Adipiscing Elit, Sed Do Eiusmod Tempor Incididunt Ut</p></div>
  <div class="svc" style="left:784px;top:2080px"><div class="img" role="img" aria-label="Gloved hands disinfecting a dental chair"></div><h4>Medical &amp; Dental Facility Cleaning</h4><p>Lorem Ipsum Dolor Sit Amet, Consectetur Adipiscing Elit, Sed Do Eiusmod Tempor Incididunt Ut</p></div>
  <div class="svc" style="left:82px;top:2517px"><div class="img" role="img" aria-label="Janitor mopping a residential hallway"></div><h4>Multi-Unit Residential Janitorial</h4><p>Lorem Ipsum Dolor Sit Amet, Consectetur Adipiscing Elit, Sed Do Eiusmod Tempor Incididunt Ut</p></div>
  <div class="svc" style="left:433px;top:2517px"><div class="img" role="img" aria-label="Cleaner washing glass windows"></div><h4>Window Cleaning</h4><p>Lorem Ipsum Dolor Sit Amet, Consectetur Adipiscing Elit, Sed Do Eiusmod Tempor Incididunt Ut</p></div>
  <div class="svc" style="left:784px;top:2517px"><div class="img" role="img" aria-label="Carpet being vacuumed in a living area"></div><h4>Carpet &amp; Floor Care</h4><p>Lorem Ipsum Dolor Sit Amet, Consectetur Adipiscing Elit, Sed Do Eiusmod Tempor Incididunt Ut</p></div>

  <!-- industries -->
  <div class="abs label center" style="top:3025px">Industries We Served</div>
  <div class="abs h2 center" style="top:3060px;font-size:38px">Solutions Built For Every Space</div>
  <div class="ind" style="left:82px"><i></i>Office</div>
  <div class="ind" style="left:293px"><i></i>Healthcare</div>
  <div class="ind on" style="left:503px"><i></i>Retail</div>
  <div class="ind" style="left:714px"><i></i>Education</div>
  <div class="ind" style="left:924px"><i></i>Industrial</div>

  <!-- property management -->
  <div class="abs" style="left:0;top:3358px;width:1200px;height:558px;background:var(--blue)"></div>
  <div class="photo" style="left:0;top:3358px;width:1200px;height:558px;background:linear-gradient(120deg,#4d5a5a,#9aa39a 45%,#cfc7bd);clip-path:polygon(0 0,68% 0,58% 100%,0 100%)" role="img" aria-label="Property managers meeting clients at a table with a laptop"></div>
  <div class="abs" style="left:841px;top:3510px;width:280px;color:#fff">
    <div style="font-size:40px;font-weight:600;line-height:1.25">Property Management</div>
    <p style="font-size:12.5px;line-height:1.8;margin:22px 0 30px;opacity:.9">Lorem Ipsum Dolor Sit Amet, Consectetur Adipiscing Elit, Sed Do Eiusmod Tempor Incididunt Ut</p>
    <span class="btn" style="padding:0 28px">Request a Free Quote</span>
  </div>

  <!-- why choose -->
  <div class="abs" style="left:82px;top:4030px;width:340px">
    <div class="label">Why Choose Harbor</div>
    <div class="h2" style="margin:12px 0 34px">Trusted. Trained. Proven</div>
    <ul class="ticks">
      <li>Consistent, High-Quality Service</li><li>Trained &amp; Trustworthy Staff</li><li>Flexible Scheduling</li><li>Eco-Friendly Cleaning Options</li><li>100% Satisfaction Guarantee</li>
    </ul>
    <span class="btn" style="margin-top:36px;padding:0 34px">Learn More</span>
  </div>
  <div class="photo" style="left:518px;top:4011px;width:600px;height:394px;background:linear-gradient(150deg,#eef0f2,#9aa3ad 60%,#3b4452);clip-path:polygon(0 13%,100% 0,100% 100%,0 100%)" role="img" aria-label="Business team gathered around a laptop in a meeting room"></div>
  <div class="abs" style="left:433px;top:4310px;width:181px;height:85px;background:var(--blue);color:#fff;padding:14px 18px;border:5px solid #fff"><div style="font-size:22px;font-weight:700">10+</div><div style="font-size:9px;opacity:.85">Lorem Ipsum Dolor Sit Amet</div></div>

  <!-- plans -->
  <div class="abs" style="left:0;top:4501px;width:1200px;height:760px;background:var(--soft)"></div>
  <div class="abs label center" style="top:4594px">Choose Your Plan</div>
  <div class="abs h2 center" style="top:4628px;font-size:38px">Choose Your Perfect Clean</div>
  <div class="plan" style="left:82px"><div class="t"><i></i>Basic Plan</div><div class="amt"><small style="font-size:20px">$</small>30 <small>monthly</small></div><ul class="ticks"><li>Lorem Ipsum Dolor Sit Amet</li><li>Lorem Ipsum Dolor Sit Amet</li><li>Lorem Ipsum Dolor Sit Amet</li><li>Lorem Ipsum Dolor Sit Amet</li><li>Lorem Ipsum Dolor Sit Amet</li></ul><span class="btn">Buy Plan</span></div>
  <div class="plan" style="left:433px"><div class="t"><i></i>Standard Plan</div><div class="amt"><small style="font-size:20px">$</small>70 <small>monthly</small></div><ul class="ticks"><li>Lorem Ipsum Dolor Sit Amet</li><li>Lorem Ipsum Dolor Sit Amet</li><li>Lorem Ipsum Dolor Sit Amet</li><li>Lorem Ipsum Dolor Sit Amet</li><li>Lorem Ipsum Dolor Sit Amet</li></ul><span class="btn">Buy Plan</span></div>
  <div class="plan on" style="left:784px"><div class="t"><i></i>Premium Plan</div><div class="amt"><small style="font-size:20px">$</small>120 <small>monthly</small></div><ul class="ticks"><li>Lorem Ipsum Dolor Sit Amet</li><li>Lorem Ipsum Dolor Sit Amet</li><li>Lorem Ipsum Dolor Sit Amet</li><li>Lorem Ipsum Dolor Sit Amet</li><li>Lorem Ipsum Dolor Sit Amet</li></ul><span class="btn">Buy Plan</span></div>

  <!-- testimonials -->
  <div class="abs label center" style="top:5355px">Testimonials</div>
  <div class="abs h2 center" style="top:5388px;font-size:38px">What Clients Say</div>
  <div class="photo" style="left:82px;top:5485px;width:507px;height:326px;background:linear-gradient(120deg,#e2e4e6,#8a8f96 55%,#2f3a4e)" role="img" aria-label="Two businessmen shaking hands in an office"></div>
  <div class="abs" style="left:671px;top:5515px;width:447px">
    <div style="color:var(--blue);font-size:44px;font-weight:700;line-height:1">“</div>
    <div style="color:#f6b800;font-size:14px;margin:10px 0 18px">★★★★★</div>
    <p class="p" style="font-size:12.5px;color:#333">Lorem Ipsum Dolor Sit Amet, Consectetur Adipiscing Elit, Sed Do Eiusmod Tempor Incididunt Ut Labore Et Dolore Magna Aliqua. Ut Enim Ad Minim Veniam, Quis Nostrud Exercitation Ullamco Laboris Nisi Ut Aliquip Ex Ea Commodo Consequat. Duis Aute Irure Dolor In Reprehenderit In Voluptate Velit Esse Cillum Dolore Eu Fugiat Nulla Pariatur. Excepteur Sint Occaecat Cupidatat Non Proident.</p>
    <div style="color:var(--blue);font-size:44px;font-weight:700;text-align:right;line-height:1;margin-top:6px">”</div>
  </div>
  <div class="abs" style="left:220px;top:5838px;display:flex;gap:6px"><span style="width:45px;height:3px;background:#ccc"></span><span style="width:45px;height:3px;background:#ccc"></span><span style="width:45px;height:3px;background:#ccc"></span><span style="width:45px;height:3px;background:var(--blue)"></span><span style="width:45px;height:3px;background:#ccc"></span></div>

  <!-- cta -->
  <div class="photo" style="left:82px;top:5936px;width:1036px;height:426px;background:linear-gradient(180deg,#2356c8,#1b49b3 55%,#2a5cc4)" role="img" aria-label="City bridge over water tinted in blue"></div>
  <div class="abs center" style="top:6060px;color:#fff">
    <div style="font-size:40px;font-weight:600">Experience A Cleaner Workplace Today</div>
    <p style="font-size:12.5px;line-height:1.8;margin:10px auto 34px;width:720px;opacity:.9">Lorem Ipsum Dolor Sit Amet, Consectetur Adipiscing Elit, Sed Do Eiusmod Tempor Incididunt Ut Labore Et Dolore Magna Aliqua. Ut Enim Ad Minim Veniam, Quis Nostrud Exercitation Ullamco Laboris Nisi Ut Aliquip Ex Ea</p>
    <span class="btn">Request a Free Quote</span>
    <span class="btn" style="background:transparent;border:2px solid #fff;margin-left:6px">Book a Walkthrough</span>
  </div>

  <!-- contact strip -->
  <div class="abs center" style="top:6446px;display:flex;justify-content:center;align-items:center;gap:40px">
    <span style="color:var(--blue);font-style:italic;font-weight:500;font-size:20px">Contact Us Today For A <u>Free Case Evaluation?</u></span>
    <span class="btn">Free Consultation</span>
  </div>

  <!-- footer -->
  <div class="abs" style="left:82px;top:6545px;width:300px">
    <div class="brand"><span class="mark"></span>HARBOR SWEEP TEAM</div>
    <p class="p" style="font-size:12px;color:#333;margin-top:34px">Lorem Ipsum Dolor Sit Amet, Consectetur Adipiscing Elit, Sed Do Eiusmod Tempor Incididunt Ut Labore Et Dolore Magna</p>
  </div>
  <div class="abs" style="left:510px;top:6530px;width:1px;height:170px;background:var(--line)"></div>
  <div class="abs flinks" style="left:543px;top:6532px"><b style="font-weight:600">Quick Links</b><br><br>Home<br>About Us<br>Services<br>Industries Served<br>Testimonials<br>Contact Us</div>
  <div class="abs" style="left:810px;top:6530px;width:1px;height:170px;background:var(--line)"></div>
  <div class="abs" style="left:845px;top:6532px;width:273px">
    <div style="font-size:12px;font-weight:600">Subscribe Our Newsletter</div>
    <div style="display:flex;margin-top:28px"><span style="flex:1;height:40px;border:1px solid var(--line);font-size:11px;color:var(--muted);display:flex;align-items:center;padding-left:14px">Email</span><span class="btn" style="height:40px;padding:0 24px">Sign Up</span></div>
    <div style="margin-top:30px"><span class="dot"></span><span class="dot"></span><span class="dot"></span><span class="dot"></span><span class="dot"></span><span class="dot"></span></div>
  </div>
  <div class="abs" style="left:82px;top:6720px;width:1036px;height:1px;background:var(--line)"></div>
  <div class="abs center" style="top:6752px;font-size:12px">Copyright ©2025 Cleaning Company - All Rights Reserved</div>

</div>
</body>
</html>
```